Varelto Stationary and Branding Documents

Corporate Identity Branding stationary needed for IT Recruiting Firm.

I already have a Logo, business cards and website. I need to get designs completed for the remaining corporate identity documents.

The documentation should use similar colors as my website and business card. The designs should modern and clean.

http://varelto-example.com/

Target Market(s)

Information Technology Industry

Industry/Entity Type

Information Technology

Colors
3377b5
0255a3
fbee3e
f78f20
f37122
33a6d7
000000
0592cd

Requirements
Must have
• Letter Head
• Folder Design
• PowerPoint Design
• Invoice
• Envelope
Nice to have
• Proposal
• Flyer
• Brochure
Should not have
• Logo
• Business Cards
• Website

```html
<!DOCTYPE html>
<html lang="en">
<head>
<meta charset="utf-8">
<title>Varelto Stationery Set</title>
<link rel="stylesheet" href="https://fonts.googleapis.com/css2?family=Arimo:wght@400;500&display=swap">
<style>
:root{
  --board:#9a9794;
  --paper:#ffffff;
  --brand-blue:#0255a3;
  --brand-orange:#f37122;
  --accent-sky:#33a6d7;
  --ink:#1f2a44;
  --label:#1b1b1b;
  --rule:#f4b68a;
  --head-fill:#d8ecfa;
}
*{box-sizing:border-box;margin:0;padding:0}
html,body{width:1200px;height:897px;overflow:hidden;background:var(--board)}
body{position:relative;font-family:"Arimo",Arial,sans-serif;color:var(--ink)}
.label{position:absolute;font-size:19px;color:var(--label);letter-spacing:.2px}
.sheet{position:absolute;background:var(--paper);overflow:hidden}
.bar{position:absolute}
.bar--blue{background:var(--brand-blue)}
.bar--orange{background:var(--brand-orange)}
.brand{position:absolute;line-height:1}
.brand__name{display:block;color:var(--brand-blue);font-weight:400;letter-spacing:.5px}
.brand__tag{display:block;color:var(--ink);margin-top:2px;letter-spacing:.3px}
.brand--center{text-align:center;transform:translateX(-50%)}
.contact-row{position:absolute;display:flex;align-items:center;gap:5px;white-space:nowrap;color:var(--ink)}
.contact-row span,.contact-list li{display:inline-flex;align-items:center;gap:2px}
.icon{display:inline-block;flex:none}
.contact-list{position:absolute;list-style:none;font-size:7px;line-height:9.5px}

/* invoice */
.invoice-title{position:absolute;left:146px;top:63px;transform:translateX(-50%);font-size:9px;letter-spacing:2.5px;color:var(--accent-sky);font-weight:500}
.field{position:absolute;border:1px solid var(--rule);font-size:7px;padding:8px 5px}
.field__line{position:absolute;left:17px;right:6px;height:1px;background:#b9b9b9}
.items{position:absolute;left:20px;top:134px;width:259px;border-collapse:collapse;font-size:7px;table-layout:fixed}
.items th{background:var(--head-fill);font-weight:400;height:13px;border:1px solid var(--rule)}
.items td{height:18.3px;border:1px solid var(--rule)}
.items .col-sr{width:27px}
.items .col-part{width:113px}
.items .col-rate{width:60px}
</style>
</head>
<body>

<svg width="0" height="0" style="position:absolute">
  <defs>
    <symbol id="i-pin" viewBox="0 0 10 14"><path d="M5 0a5 5 0 0 1 5 5c0 3.5-5 9-5 9S0 8.5 0 5a5 5 0 0 1 5-5z" fill="#33a6d7"/><circle cx="5" cy="5" r="2" fill="#fff"/></symbol>
    <symbol id="i-phone" viewBox="0 0 10 10"><rect width="10" height="10" rx="1.5" fill="#33a6d7"/><path d="M3 2.5l1 1.5-.6.8a4 4 0 0 0 1.8 1.8l.8-.6 1.5 1-.5 1C4.5 8 2 5.5 2 3z" fill="#fff"/></symbol>
    <symbol id="i-mail" viewBox="0 0 10 10"><rect width="10" height="10" rx="1.5" fill="#33a6d7"/><rect x="2" y="3" width="6" height="4" fill="none" stroke="#fff" stroke-width=".8"/><path d="M2 3l3 2.3L8 3" fill="none" stroke="#fff" stroke-width=".8"/></symbol>
    <symbol id="i-web" viewBox="0 0 10 10"><rect width="10" height="10" rx="1.5" fill="#33a6d7"/><circle cx="5" cy="5" r="3" fill="none" stroke="#fff" stroke-width=".8"/><path d="M2 5h6M5 2v6" stroke="#fff" stroke-width=".6"/></symbol>
  </defs>
</svg>

<!-- Envelope -->
<div class="label" style="left:110px;top:56px">ENVELOPE</div>
<section class="sheet envelope" style="left:106px;top:80px;width:513px;height:227px">
  <div class="bar bar--blue" style="left:485px;top:0;width:5px;height:55px"></div>
  <div class="bar bar--orange" style="left:494px;top:0;width:5px;height:55px"></div>
  <div class="bar bar--blue" style="left:9px;top:183px;width:5px;height:44px"></div>
  <div class="bar bar--orange" style="left:19px;top:183px;width:5px;height:44px"></div>
  <div class="brand" style="left:29px;top:183px">
    <span class="brand__name" style="font-size:26px">varelto</span>
    <span class="brand__tag" style="font-size:7px;margin-left:12px">BUSINESS SOLUTION LLC</span>
  </div>
  <div class="contact-row" style="left:153px;top:204px;font-size:6.5px">
    <span><svg class="icon" width="5" height="7"><use href="#i-pin"/></svg>Two Harbor Plaza 410 8th Street NE</span>
    <span><svg class="icon" width="6" height="6"><use href="#i-phone"/></svg>8005550142</span>
    <span><svg class="icon" width="6" height="6"><use href="#i-mail"/></svg>info@varelto-example.com</span>
    <span><svg class="icon" width="6" height="6"><use href="#i-web"/></svg>www.varelto-example.com</span>
  </div>
</section>

<!-- PowerPoint -->
<div class="label" style="left:686px;top:56px">POWER POINT</div>
<section class="sheet slide" style="left:679px;top:79px;width:363px;height:300px">
  <div class="bar bar--blue" style="left:43px;top:0;width:5px;height:56px"></div>
  <div class="bar bar--orange" style="left:52px;top:0;width:5px;height:56px"></div>
  <div class="bar bar--blue" style="left:304px;top:270px;width:5px;height:30px"></div>
  <div class="bar bar--orange" style="left:313px;top:270px;width:5px;height:30px"></div>
  <div class="brand brand--center" style="left:181px;top:118px">
    <span class="brand__name" style="font-size:50px">varelto</span>
    <span class="brand__tag" style="font-size:14px;margin-top:3px">BUSINESS SOLUTION LLC</span>
  </div>
</section>

<!-- Letterhead -->
<div class="label" style="left:91px;top:364px">LETTER HEAD</div>
<section class="sheet letterhead" style="left:84px;top:393px;width:338px;height:436px">
  <div class="bar bar--blue" style="left:306px;top:0;width:5px;height:55px"></div>
  <div class="bar bar--orange" style="left:315px;top:0;width:5px;height:55px"></div>
  <div class="brand" style="left:25px;top:19px">
    <span class="brand__name" style="font-size:28px">varelto</span>
    <span class="brand__tag" style="font-size:7px;margin-left:12px">BUSINESS SOLUTION LLC</span>
  </div>
  <div class="bar bar--blue" style="left:5px;top:410px;width:4px;height:26px"></div>
  <div class="bar bar--orange" style="left:10px;top:410px;width:4px;height:26px"></div>
  <div class="contact-row" style="left:17px;top:418px;font-size:5.5px;gap:4px">
    <span><svg class="icon" width="5" height="6"><use href="#i-pin"/></svg>Two Harbor Plaza 410 8th Street NE</span>
    <span><svg class="icon" width="5" height="5"><use href="#i-phone"/></svg>8005550142</span>
    <span><svg class="icon" width="5" height="5"><use href="#i-mail"/></svg>info@varelto-example.com</span>
    <span><svg class="icon" width="5" height="5"><use href="#i-web"/></svg>www.varelto-example.com</span>
  </div>
</section>

<!-- Folder -->
<div class="label" style="left:466px;top:374px">FOLDER</div>
<section class="sheet folder" style="left:473px;top:397px;width:303px;height:428px">
  <div class="bar bar--blue" style="left:40px;top:0;width:13px;height:128px"></div>
  <div class="bar bar--orange" style="left:62px;top:0;width:13px;height:128px"></div>
  <div class="bar bar--blue" style="left:246px;top:366px;width:13px;height:62px"></div>
  <div class="bar bar--orange" style="left:268px;top:366px;width:13px;height:62px"></div>
  <div class="brand brand--center" style="left:150px;top:190px">
    <span class="brand__name" style="font-size:38px">varelto</span>
    <span class="brand__tag" style="font-size:11px;margin-top:3px">BUSINESS SOLUTION LLC</span>
  </div>
</section>

<!-- Invoice -->
<div class="label" style="left:840px;top:431px">INVOICE</div>
<section class="sheet invoice" style="left:824px;top:466px;width:292px;height:370px">
  <div class="brand" style="left:20px;top:21px">
    <span class="brand__name" style="font-size:28px">varelto</span>
    <span class="brand__tag" style="font-size:7px;margin-left:12px">BUSINESS SOLUTION LLC</span>
  </div>
  <ul class="contact-list" style="left:155px;top:18px">
    <li><svg class="icon" width="5" height="7"><use href="#i-pin"/></svg>Two Harbor Plaza 410 8th Street NE</li>
    <li><svg class="icon" width="6" height="6"><use href="#i-phone"/></svg>8005550142</li>
    <li><svg class="icon" width="6" height="6"><use href="#i-mail"/></svg>info@varelto-example.com</li>
    <li><svg class="icon" width="6" height="6"><use href="#i-web"/></svg>www.varelto-example.com</li>
  </ul>
  <div class="invoice-title">INVOICE</div>
  <div class="field" style="left:20px;top:74px;width:159px;height:51px">To,
    <span class="field__line" style="top:16px"></span>
    <span class="field__line" style="top:34px"></span>
  </div>
  <div class="field" style="left:185px;top:75px;width:88px;height:19px;padding:5px">Sr.</div>
  <div class="field" style="left:185px;top:100px;width:88px;height:20px;padding:6px 5px">Date</div>
  <table class="items">
    <thead><tr><th class="col-sr">Sr. No.</th><th class="col-part">Particulars</th><th class="col-rate">Rate</th><th>Amount</th></tr></thead>
    <tbody>
      <tr><td></td><td></td><td></td><td></td></tr>
      <tr><td></td><td></td><td></td><td></td></tr>
      <tr><td></td><td></td><td></td><td></td></tr>
      <tr><td></td><td></td><td></td><td></td></tr>
      <tr><td></td><td></td><td></td><td></td></tr>
      <tr><td></td><td></td><td></td><td></td></tr>
      <tr><td></td><td></td><td></td><td></td></tr>
      <tr><td></td><td></td><td></td><td></td></tr>
      <tr><td></td><td></td><td></td><td></td></tr>
      <tr><td></td><td></td><td></td><td></td></tr>
    </tbody>
  </table>
  <div class="brand" style="left:210px;top:343px">
    <span class="brand__name" style="font-size:14px">varelto</span>
    <span class="brand__tag" style="font-size:4px;margin-left:4px;margin-top:1px">BUSINESS SOLUTION LLC</span>
  </div>
</section>

</body>
</html>
```